salami or ham label design or package company image logo

we need a label design for salami. we would like to have spanish salami maker design such as finca morelló. classic and gorgeous design we like...
https://fincamorellotarn.example/ca/productes/
The target is europe market.
we want to renewal from current label design. so please see our current design and renovate new label.
better to use crown logo that we attached to the upload file.

Target Market(s)

high quality food market

Industry/Entity Type

It Company

Font styles to use
Serif
Decorative
Script

Colors
0456a4
ffffff

Requirements
Must have
• company name Korimbu must have in the label as small letters.
Nice to have
• nice to have the word like a artisan etc...maybe
Should not have
• dont need to image from Japan. Because Japanese like european design.

```html
<!DOCTYPE html>
<html lang="en">
<head>
<meta charset="utf-8">
<title>Wagyu Salami Label – Korimbu</title>
<link rel="stylesheet" href="https://fonts.googleapis.com/css2?family=Forum&family=Petit+Formal+Script&display=swap">
<style>
  :root {
    --label-blue: #0456a4;
    --label-blue-deep: #034383;
    --label-white: #ffffff;
    --frame-grey: #b9bcc0;
    --silver-light: #f2f2f2;
    --silver-mid: #c4c6c9;
    --silver-dark: #8d9095;
    --ink: #161616;
    --jewel-red: #b3121b;
  }
  html, body {
    margin: 0;
    padding: 0;
    width: 1200px;
    height: 899px;
    overflow: hidden;
    background: var(--label-white);
  }
  .canvas {
    position: relative;
    width: 1200px;
    height: 899px;
  }
  .label {
    position: absolute;
    inset: 0;
    width: 1200px;
    height: 899px;
  }
  .motto {
    font-family: "Petit Formal Script", cursive;
    font-size: 19px;
    fill: var(--label-white);
  }
  .product-name {
    font-family: "Forum", serif;
    font-size: 56px;
    fill: var(--ink);
  }
  .brand-name {
    font-family: "Forum", serif;
    font-size: 24px;
    letter-spacing: 5px;
    fill: var(--label-white);
  }
</style>
</head>
<body>
<div class="canvas">
  <svg class="label" viewBox="0 0 1200 899" xmlns="http://www.w3.org/2000/svg" aria-label="Wagyu Salami label by Korimbu">
    <defs>
      <linearGradient id="label-field" x1="0" y1="0" x2="0" y2="1">
        <stop offset="0" stop-color="var(--label-blue)"/>
        <stop offset="0.5" stop-color="#0a5fb0"/>
        <stop offset="1" stop-color="var(--label-blue-deep)"/>
      </linearGradient>
      <linearGradient id="ribbon-silver" x1="0" y1="0" x2="0" y2="1">
        <stop offset="0" stop-color="var(--silver-mid)"/>
        <stop offset="0.35" stop-color="var(--silver-light)"/>
        <stop offset="0.7" stop-color="var(--silver-mid)"/>
        <stop offset="1" stop-color="var(--silver-dark)"/>
      </linearGradient>
      <radialGradient id="jewel" cx="0.4" cy="0.35" r="0.7">
        <stop offset="0" stop-color="#e8444c"/>
        <stop offset="1" stop-color="var(--jewel-red)"/>
      </radialGradient>
    </defs>

    <!-- outer paper edge -->
    <polygon class="label-edge" points="600,82 905,450 600,818 295,450"
             fill="var(--label-white)" stroke="var(--frame-grey)" stroke-width="1.5"/>

    <!-- blue field -->
    <polygon class="label-field" points="600,100 890,450 600,800 310,450" fill="url(#label-field)"/>

    <!-- inner frame line -->
    <polygon class="label-inner-frame" points="600,128 866,450 600,772 334,450"
             fill="none" stroke="var(--label-white)" stroke-width="1.2" opacity="0.75"/>

    <!-- tip dots -->
    <circle cx="600" cy="114" r="4" fill="var(--label-white)"/>
    <circle cx="600" cy="786" r="4" fill="var(--label-white)"/>
    <circle cx="322" cy="450" r="4" fill="var(--label-white)"/>
    <circle cx="878" cy="450" r="4" fill="var(--label-white)"/>

    <!-- jewels -->
    <g class="jewel jewel-top">
      <circle cx="600" cy="160" r="14" fill="var(--silver-mid)"/>
      <circle cx="600" cy="160" r="10" fill="url(#jewel)"/>
    </g>
    <g class="jewel jewel-bottom">
      <circle cx="600" cy="740" r="14" fill="var(--silver-mid)"/>
      <circle cx="600" cy="740" r="10" fill="url(#jewel)"/>
    </g>

    <!-- crown emblem area -->
    <rect class="crown-emblem" role="img" aria-label="White crown emblem with small wings beneath"
          x="548" y="190" width="104" height="110" rx="14"
          fill="var(--label-white)" opacity="0.22"/>

    <!-- motto -->
    <text class="motto" x="600" y="350" text-anchor="middle">Nos manducare primum</text>
    <text class="motto" x="600" y="378" text-anchor="middle">ergo faciemus omne aliud</text>

    <!-- ribbon band -->
    <g class="ribbon">
      <rect x="338" y="440" width="28" height="62" fill="var(--silver-dark)"/>
      <rect x="834" y="440" width="28" height="62" fill="var(--silver-dark)"/>
      <rect x="356" y="416" width="488" height="74" rx="6" fill="url(#ribbon-silver)"/>
    </g>
    <text class="product-name" x="600" y="472" text-anchor="middle">Wagyu Salami</text>

    <!-- flourish area -->
    <rect class="flourish" role="img" aria-label="White calligraphic flourish"
          x="470" y="512" width="260" height="40" rx="20"
          fill="var(--label-white)" opacity="0.18"/>

    <!-- brand -->
    <circle class="brand-dot" cx="600" cy="604" r="8" fill="var(--label-white)"/>
    <text class="brand-name" x="600" y="648" text-anchor="middle">KORIMBU</text>
  </svg>
</div>
</body>
</html>
```